Acupuncture Medspa needs a business card design

I need a business card design that looks professional, has a spa-like quality and can offer a promo on the back. Initial promo is "First session free". The tagline of PinaVell is: Unwind, Mend, Glow.

PinaVell is a membership-based acupuncture medspa that offers acupuncture, cupping, and herbal therapies. Members choose between the "Refresh" membership which is for stress relief, or "Restore" which is for treating health conditions, and lastly "Rejuvenate" which is for natural facial enhancement.

Industry/Entity Type

Health And Wellness

Contact Information for Business Card

Doris Kettle, MAC, L.Ac.
614-385-2097
www.pinavell-example.com

Font styles to use
Serif
Sans Serif

Colors

Designer to choose colors to be used in the design.

Requirements
Must have
• The project must have PinaVell logo, promo on the back, and contact information
Nice to have
• I would like to see the colors of the logo used.

```html
<!DOCTYPE html>
<html lang="en">
<head>
<meta charset="utf-8">
<title>PinaVell Business Card</title>
<link href="https://fonts.googleapis.com/css2?family=Lato:wght@400;700&display=swap" rel="stylesheet">
<style>
  :root {
    --backdrop: #2a2a2a;
    --paper: #ffffff;
    --teal: #1f8a83;
    --teal-deep: #23817a;
    --teal-card: #008a80;
    --ink: #333333;
    --rule: #7a7a7a;
    --white: #ffffff;
  }
  * { margin: 0; padding: 0; box-sizing: border-box; }
  html, body {
    width: 1200px; height: 1200px; overflow: hidden;
    background: var(--backdrop);
    font-family: "Lato", Arial, sans-serif;
  }
  .stage { position: relative; width: 1200px; height: 1200px; }
  .card {
    position: absolute; top: 310px; height: 594px;
  }
  .card-front { left: 234px; width: 364px; background: var(--paper); }
  .card-back { left: 627px; width: 369px; background: var(--teal-card); }

  .brand {
    position: absolute; left: 0; right: 0; top: 462px; top: 152px;
    display: flex; align-items: center; justify-content: center; gap: 12px;
  }
  .brand-mark {
    width: 36px; height: 36px; border-radius: 50%;
    border: 3px solid var(--teal);
  }
  .brand-name {
    font-weight: 700; font-size: 40px; letter-spacing: 2px;
    color: var(--teal);
  }

  .holder-name {
    position: absolute; left: 0; right: 0; top: 338px;
    text-align: center; font-size: 20px; font-weight: 400;
    color: var(--teal-deep);
  }
  .contact-icons {
    position: absolute; left: 87px; top: 385px; width: 190px; height: 26px;
  }
  .contact-list {
    position: absolute; left: 0; right: 0; top: 420px;
    text-align: center; font-size: 17px; line-height: 22px; color: var(--ink);
    list-style: none;
  }
  .divider {
    position: absolute; left: 87px; width: 190px; top: 502px;
    height: 1px; background: var(--rule);
  }
  .tagline {
    position: absolute; left: 0; right: 0; top: 524px;
    text-align: center; font-size: 15px; letter-spacing: 0.3px; color: var(--ink);
  }

  .back-emblem {
    position: absolute; left: 80px; top: 193px; width: 208px; height: 208px;
    border: 4px solid var(--white); border-radius: 50%;
    display: flex; align-items: center; justify-content: center;
  }
  .back-emblem-name {
    font-weight: 700; font-size: 30px; letter-spacing: 2px; color: var(--white);
  }
  .promo {
    position: absolute; left: 0; right: 0; top: 526px;
    text-align: center; font-size: 18px; font-weight: 700; color: var(--white);
  }
</style>
</head>
<body>
<main class="stage">
  <section class="card card-front" aria-label="Business card front">
    <div class="brand">
      <span class="brand-mark" aria-hidden="true"></span>
      <span class="brand-name">PINAVELL</span>
    </div>

    <h1 class="holder-name">DORIS KETTLE, MAC, L.AC.</h1>

    <svg class="contact-icons" viewBox="0 0 190 26" aria-hidden="true">
      <line x1="0" y1="13" x2="54" y2="13" stroke="#7a7a7a" stroke-width="1"/>
      <line x1="136" y1="13" x2="190" y2="13" stroke="#7a7a7a" stroke-width="1"/>
      <circle cx="67" cy="13" r="12" fill="#1f8a83"/>
      <circle cx="94" cy="13" r="12" fill="#1f8a83"/>
      <circle cx="121" cy="13" r="12" fill="#1f8a83"/>
      <!-- phone -->
      <path d="M61 10 q6 -4 12 0 l-1 2 h-2 v-1 h-6 v1 h-2 z M62 13 h10 v4 h-10 z" fill="#fff"/>
      <!-- envelope -->
      <rect x="87.5" y="8.5" width="13" height="9" fill="none" stroke="#fff" stroke-width="1.4"/>
      <path d="M87.5 8.5 l6.5 5 l6.5 -5" fill="none" stroke="#fff" stroke-width="1.4"/>
      <!-- globe -->
      <circle cx="121" cy="13" r="6" fill="none" stroke="#fff" stroke-width="1.4"/>
      <ellipse cx="121" cy="13" rx="2.5" ry="6" fill="none" stroke="#fff" stroke-width="1.1"/>
      <line x1="115" y1="13" x2="127" y2="13" stroke="#fff" stroke-width="1.1"/>
    </svg>

    <ul class="contact-list">
      <li>614-385-2097</li>
      <li>doriskettle@pinavell-example.com</li>
      <li>www.pinavell-example.com</li>
    </ul>

    <div class="divider" aria-hidden="true"></div>

    <p class="tagline">UNWIND | MEND | GLOW</p>
  </section>

  <section class="card card-back" aria-label="Business card back">
    <div class="back-emblem">
      <span class="back-emblem-name">PINAVELL</span>
    </div>
    <p class="promo">FIRST SESSION FREE</p>
  </section>
</main>
</body>
</html>
```